Need A Modern Website Design For ADSL2+ Provider

AIM: To sell affordable combined ADSL2+ Unlimited & phone line rentals to residential customers.

TYPE: This project is for DESIGN only (no code)

Source Files: I need all source files, fonts, images to be provided in ZIP format.

Logo: Existing (attached)

-Corporate Colours-
Black & Red (Same as Logo)
Others colours are fine as long as it looks corporate and modern.

-Pages-
Need another page to display our pricing plan

(1)Homepage Design
(2)Page to display our plans (needs to be in tables)
Example: http://lnkbrev.example/QwTr8k

-Pricing Plan-
(1) $59.95 / Month (Metro / City Areas)
(2) $79.95 / Month (Outside City Areas / Rural Areas)
Detailed Pricing plans is in PDF attached
Updates

Target Market(s)

Both male & female, Young & Old

Industry/Entity Type

Residential

Requirements
Must have
• + Graphic banner on the home page that shows our ADSL2+ combo plan for ADSL2+ Unlimited & Phone Line Rental for only $59.95

+ A box to allow customers to login to their account (username & password + login button)

+ Clearly display contact number
+ Button to sign up
+ Button to check service availability something like https://checkin.pelwara.example/wizard/

+ Button for Live Chat
+ Navigation menu
+ Social media icons plain square, Google +, plain square
+ Minimal text on homepage
+ Corporate & Friendly
Nice to have
• + Effective use of icons with corporate colours
+ Effective use of stockphotos
(use of people in photos would be nice)

+ Effective use of graphics to navigate people through the site and inform customers of specials,etc.
Should not have
• + Cluttered
+ Don’t want long scrolling homepage
+ Don’t want too much text on homepage 500 words is the estimate max.

```html
<!DOCTYPE html>
<html lang="en">
<head>
<meta charset="utf-8">
<title>Tarnvale – Unlimited ADSL2+ Broadband</title>
<link rel="stylesheet" href="https://fonts.googleapis.com/css2?family=Open+Sans:ital,wght@0,300;0,400;0,600;1,400&display=swap">
<style>
:root{
  --red:#e8312c;
  --red-dark:#b9141a;
  --ink:#222;
  --hero:#2b2b2b;
  --hero-deep:#1d1d1d;
  --muted:#666;
  --line:#d9d9d9;
  --panel:#f3f3f3;
  --footer:#ececec;
}
*{box-sizing:border-box;margin:0;padding:0}
html,body{width:758px;height:1200px;overflow:hidden;background:#fff}
body{position:relative;font-family:"Open Sans",Arial,sans-serif;color:var(--ink)}
.abs{position:absolute}

/* header */
.brand{left:64px;top:12px;display:flex;align-items:center;gap:8px}
.brand-dot{width:46px;height:46px;border-radius:50%;background:var(--ink)}
.brand-name{font-size:28px;font-weight:400;color:var(--ink);letter-spacing:2px}
.top-btn{top:14px;height:15px;font-size:9px;color:#fff;display:flex;align-items:center;justify-content:center}
.btn-chat{left:442px;width:68px;background:#1e1e1e}
.btn-signup{left:517px;width:68px;background:var(--red)}
.phone{left:598px;top:12px;font-size:12.5px;display:flex;align-items:center;gap:4px}
.nav{left:357px;top:42px;width:338px;height:22px;background:var(--ink);display:flex}
.nav a{font-size:8.5px;color:#ccc;text-decoration:none;display:flex;align-items:center;justify-content:center;height:100%}
.nav a.active{background:var(--red);color:#fff}

/* hero */
.hero{left:0;top:64px;width:758px;height:283px;background:var(--hero)}
.hero-frame{left:64px;top:104px;width:632px;height:204px;border-radius:102px;border:9px solid #454545;background:var(--hero-deep)}
.product-disc{left:84px;top:120px;width:172px;height:172px;border-radius:50%;background:#fff}
.product-shot{left:108px;top:145px;width:124px;height:115px;border-radius:10px;background:radial-gradient(ellipse at 50% 70%,#9a9a9a,#d8d8d8 60%,#fff 80%)}
.hero-title{left:270px;top:131px;font-size:36px;font-weight:300;color:var(--red);line-height:1}
.hero-sub{left:269px;top:170px;font-size:15.5px;color:#fff}
.hero-rule{left:442px;top:140px;width:1px;height:64px;background:var(--red)}
.price{left:454px;top:131px;color:var(--red);font-size:35px;font-weight:300;line-height:1}
.price-cents{left:524px;top:134px;font-size:21px;color:#fff;font-weight:300;line-height:1}
.price-unit{left:524px;top:157px;font-size:10px;color:#fff}
.price-note{left:456px;top:176px;font-size:10px;color:#ddd;line-height:14px}
.badge{left:570px;top:104px;width:126px;height:64px;border-radius:24px;background:#fff;border:2px solid var(--red);text-align:center;padding-top:14px}
.badge b{display:block;font-weight:400;font-size:11.5px;color:var(--ink);line-height:14px}
.badge span{display:block;font-size:10px;color:var(--red);line-height:14px}
.combo-row{left:270px;top:210px;display:flex;align-items:baseline;gap:4px;white-space:nowrap}
.combo{font-size:25px;color:var(--red);font-weight:400;line-height:1}
.combo-line{font-size:10px;color:#fff}
.hero-fine{left:270px;top:248px;font-size:8.5px;color:#eee;line-height:14px;width:300px}

/* plan tabs */
.tabs{left:0;top:347px;width:758px;height:47px;background:linear-gradient(#d6262a,var(--red-dark))}
.tab{top:347px;height:47px;display:flex;align-items:center;justify-content:center;font-size:13.5px;color:#fff;border-left:1px solid #8f0f13}
.tab.last{border-right:1px solid #8f0f13}

/* availability */
.avail{left:62px;top:418px;width:632px;height:71px;background:var(--panel);border:1px solid var(--line)}
.avail-input{left:145px;top:426px;width:352px;height:24px;background:#fff;border:1px solid var(--line);font-size:11px;color:#aaa;padding:5px 6px}
.avail-btn{left:502px;top:426px;width:179px;height:24px;background:var(--red);color:#fff;font-size:12.5px;display:flex;align-items:center;justify-content:center}
.avail-note{left:145px;top:456px;font-size:8px;color:#888}
.avail-opt{left:145px;top:472px;font-size:7px;color:#888;display:flex;align-items:center;gap:4px}
.box{width:8px;height:8px;border:1px solid #4a6fa5;background:#fff}
.avail-help{left:409px;top:472px;font-size:7px;color:#888}
.avail-help b{color:var(--red);font-weight:400}

/* plans table */
.plans{left:62px;top:514px;width:632px;border-collapse:collapse;border:1px solid #ccc}
.plans th{height:39px;background:linear-gradient(#4a4a4a,#1e1e1e);color:#fff;font-weight:400;font-size:14px;line-height:1;border-left:1px solid #111}
.plans th small{display:block;font-size:8px;margin-top:2px}
.plans th small.tiny{font-size:6px}
.plans td{font-size:7px;text-align:center;line-height:9px;border-top:1px solid #fff;background:#efefef;padding:0 6px}
.plans td.label{text-align:left;background:#e5e5e5;padding-left:19px;width:216px}
.plans tr.accent td.label{color:var(--red)}
.plans td.red{color:var(--red)}
.plans td.big{font-size:14px;color:var(--red)}
.plans td+td{border-left:1px solid #d6d6d6}

/* welcome + login */
.welcome-title{left:63px;top:880px;font-size:19px;color:var(--red);font-weight:400}
.welcome-text{left:64px;top:912px;width:410px;font-size:8.6px;line-height:17.6px;color:#444}
.field{left:484px;width:205px;height:24px;border:1px solid #ccc;background:#fff;font-size:8.5px;color:#999;padding:6px 6px}
.login-btn{left:634px;top:976px;width:53px;height:19px;background:#222;color:#fff;font-size:8.5px;display:flex;align-items:center;justify-content:center;border-radius:2px}

/* footer */
.footer{left:0;top:1021px;width:758px;height:179px;background:var(--footer);border-top:4px solid #e2e2e2}
.foot-col{top:1037px}
.foot-col h4{font-size:9.5px;font-weight:400;color:#222;margin-bottom:8px}
.foot-col a{display:block;font-size:7.2px;color:#555;line-height:13.4px;text-decoration:underline}
.social{display:flex;gap:10px;margin-bottom:12px}
.social span{width:19px;height:19px;background:#3a6ea5;border-radius:2px}
.social span.sq2{background:#4aa3d8}
.social span.sq3{background:#1e6fa8}
.news{display:flex;margin-top:8px}
.news-input{width:114px;height:18px;background:#e0e0e0;font-size:6.5px;font-style:italic;color:#888;padding:5px 7px}
.news-btn{width:53px;height:18px;background:var(--red);color:#fff;font-size:8px;display:flex;align-items:center;justify-content:center}
.foot-rule{left:63px;top:1168px;width:632px;height:1px;background:#d6d6d6}
.copy{left:63px;top:1179px;font-size:7.5px;color:#888}
</style>
</head>
<body>

<!-- header -->
<div class="abs brand"><span class="brand-dot"></span><span class="brand-name">TARNVALE</span></div>
<div class="abs top-btn btn-chat">Live Chat</div>
<div class="abs top-btn btn-signup">Sign Up</div>
<div class="abs phone">
  <svg width="11" height="11" viewBox="0 0 24 24"><path fill="#e8312c" d="M6.6 10.8a15 15 0 0 0 6.6 6.6l2.2-2.2c.3-.3.7-.4 1-.2 1.1.4 2.3.6 3.6.6.6 0 1 .4 1 1V20c0 .6-.4 1-1 1A17 17 0 0 1 3 4c0-.6.4-1 1-1h3.5c.6 0 1 .4 1 1 0 1.3.2 2.5.6 3.6.1.3 0 .7-.2 1z"/></svg>
  <span>1300 55 18 40</span>
</div>
<nav class="abs nav">
  <a class="active" style="width:59px">Home</a>
  <a style="width:63px">Features</a>
  <a style="width:68px">About Us</a>
  <a style="width:66px">Services</a>
  <a style="width:82px">Contact Us</a>
</nav>

<!-- hero -->
<div class="abs hero"></div>
<div class="abs hero-frame"></div>
<div class="abs product-disc"></div>
<div class="abs product-shot" role="img" aria-label="Wireless ADSL2+ modem router"></div>
<div class="abs hero-title">Unlimited</div>
<div class="abs hero-sub">ADSL2+ BROADBAND</div>
<div class="abs hero-rule"></div>
<div class="abs price">$ 59</div>
<div class="abs price-cents">.95</div>
<div class="abs price-unit">/month</div>
<div class="abs price-note">$1.89 for first 20 minutes then<br>per minute rate applies</div>
<div class="abs badge"><b>‘NO’ SETUP FEE</b><span>Modem Included</span></div>
<div class="abs combo-row"><span class="combo">Pairline+</span><span class="combo-line">offers line rental with Unlimited ADSL2+ Broadband.</span></div>
<div class="abs hero-fine">$250 if any part of service is cancelled or transferred before the end of the<br>24 month term</div>

<!-- plan tabs -->
<div class="abs tabs"></div>
<div class="abs tab" style="left:62px;width:232px">ADSL2+ With Home Phone</div>
<div class="abs tab" style="left:294px;width:172px">ADSL2+</div>
<div class="abs tab last" style="left:466px;width:229px">Broad Band Off-net</div>

<!-- availability -->
<div class="abs avail"></div>
<svg class="abs" style="left:74px;top:426px" width="56" height="56" viewBox="0 0 56 56">
  <circle cx="20" cy="20" r="16" fill="#fff" stroke="#bbb" stroke-width="3"/>
  <line x1="32" y1="32" x2="50" y2="50" stroke="#999" stroke-width="5" stroke-linecap="round"/>
  <circle cx="20" cy="20" r="5" fill="#888"/>
</svg>
<div class="abs avail-input">Enter your phone number</div>
<div class="abs avail-btn">Check service availability</div>
<div class="abs avail-note">By entering a number you agree that Tarnvale may contact you to discuss the availability of services in your area.</div>
<div class="abs avail-opt"><span class="box"></span>Please do not call me</div>
<div class="abs avail-help">No home phone? Click <b>Here</b></div>

<!-- plans table -->
<table class="abs plans">
  <tr>
    <th style="width:216px">Pairline+ Plans<small>Effective 1 January 2013</small></th>
    <th style="width:212px">Metro<small>On Net</small></th>
    <th>Regional<small class="tiny">Off Net<br>(If Metro on-net not available)</small></th>
  </tr>
  <tr style="height:35px"><td class="label">Minimum Monthly Charge, including line rental<br>and Unlimited ADSL2+</td><td class="big">$59.95</td><td class="big">$79.95</td></tr>
  <tr class="accent" style="height:18px"><td class="label">Local Calls</td><td>18cents/call</td><td>18cents/call</td></tr>
  <tr style="height:27px"><td class="label">National Long Distance Calls (per minute)<br>Plus Cap National long Distance calls</td><td class="red">29cents $1.89 for first 20 minutes<br>then per minute rate applies</td><td class="red">29cents $1.89 for first 20 minutes<br>then per minute rate applies</td></tr>
  <tr class="accent" style="height:26px"><td class="label">Calls to Mobiles within Australia (per minute)<br>Plus Cap Calls to mobile</td><td>35cents $3.40 for the first 20 minutes then<br>per minute rate applies</td><td>35cents $3.40 for the first 20 minutes then<br>per minute rate applies</td></tr>
  <tr style="height:18px"><td class="label">13/1300 Calls per call</td><td class="red">44cents</td><td class="red">44cents</td></tr>
  <tr class="accent" style="height:18px"><td class="label">International calls</td><td>Refer standard rates sheet</td><td>Refer standard rates sheet</td></tr>
  <tr style="height:18px"><td class="label">Call Connection fee (timed calls)</td><td class="red">39 cents per call</td><td class="red">39 cents per call</td></tr>
  <tr class="accent" style="height:18px"><td class="label">Contract term</td><td>24months</td><td>24months</td></tr>
  <tr style="height:27px"><td class="label">Minimum 24 month contract cost including Delivery<br>and Handling fee for the WiFi modem</td><td class="red">$1,463.75</td><td class="red">$1,943.75</td></tr>
  <tr class="accent" style="height:19px"><td class="label">WiFi Modem (included in cost)</td><td>No Charge</td><td>No Charge</td></tr>
  <tr style="height:18px"><td class="label">Delivery and Handling fee of Modem</td><td class="red">One off charge of $24.95</td><td class="red">One off charge of $24.95</td></tr>
  <tr class="accent" style="height:18px"><td class="label">Set up fee</td><td>No Charge</td><td>No Charge</td></tr>
  <tr style="height:22px"><td class="label">Termination fee</td><td class="red">$250 if any part of service is cancelled or<br>transferred before the end of the 24 month term</td><td class="red">$250 if any part of service is cancelled or<br>transferred before the end of the 24 month term</td></tr>
  <tr class="accent" style="height:26px"><td class="label">Administration fee (per month)</td><td>$10 administration fee if preselected to<br>other service provider</td><td>$10 administration fee if preselected to<br>other service provider</td></tr>
</table>

<!-- welcome + login -->
<h1 class="abs welcome-title">Welcome to Tarnvale</h1>
<p class="abs welcome-text">Contrairement à une opinion répandue, le Lorem Ipsum n'est pas simplement du texte aléatoire. Il trouve ses racines dans une oeuvre de la littérature latine classique datant de 45 av. J.-C., le rendant vieux de 2000 ans. Un professeur du Marlow-Keene College, en Virginie, s'est intéressé à un des mots latins les plus obscurs, consectetur, extrait d'un passage.</p>
<div class="abs field" style="top:892px">User Name</div>
<div class="abs field" style="top:935px">Password</div>
<div class="abs login-btn">Login</div>

<!-- footer -->
<footer class="abs footer"></footer>
<div class="abs foot-col" style="left:63px">
  <h4>Company</h4>
  <a>Contrairement</a><a>Opinion répandue</a><a>Pas simplement du</a><a>Texte aléatoire</a>
</div>
<div class="abs foot-col" style="left:231px">
  <h4>Dictionnaire de</h4>
  <a>Plusieurs variations</a><a>De Lorem Ipsum</a><a>Vent être</a>
</div>
<div class="abs foot-col" style="left:399px">
  <h4>Embarassantes</h4>
  <a>L'extrait standard</a><a>Utilisé depuis</a><a>Siècle est reproduit</a><a>Dessous pour les</a><a>Curieux</a><a>Vous voulez utiliser</a><a>Passage du Lorem</a>
</div>
<div class="abs foot-col" style="left:526px">
  <h4>Stay updates on our Socail Network</h4>
  <div class="social"><span></span><span class="sq2"></span><span class="sq3"></span></div>
  <h4>Join Our Newsletter</h4>
  <div class="news"><div class="news-input">Enter your email address</div><div class="news-btn">Subscribe</div></div>
</div>
<div class="abs foot-rule"></div>
<div class="abs copy">© Copyrights 2013 All rights Reserved</div>

</body>
</html>
```